Business Card design for Brightvale Global

we need a business card design for our company. we are a trading company based in LA.

Company Name: Brightvale Global Corp.
Contact: Marla Ostrov
Title: CEO
Tel: 310-447-2093
Email: bvgcorp7@mailnest.example

Target Market(s)

International, especially China

Industry/Entity Type

Trade

Colors
3276b5
34a7d8
0555a3
0493ce
85cae6
85acd3
d0dfed
cee9f5

Requirements
Must have
• Logo and contact, to have international/global feeling

```html
<!DOCTYPE html>
<html lang="en">
<head>
<meta charset="utf-8">
<title>Brightvale Global – Business Card</title>
<link rel="stylesheet" href="https://fonts.googleapis.com/css2?family=Open+Sans:wght@400;600;700&family=Roboto+Condensed:wght@700&display=swap">
<style>
  :root {
    --stage: #232427;
    --card-white: #f4f4f4;
    --navy: #1b3358;
    --brand-blue: #0555a3;
    --sky: #3276b5;
    --bright: #34a7d8;
    --deep: #0f3c70;
    --rule: #85acd3;
    --text-grey: #444;
  }
  * { margin: 0; padding: 0; box-sizing: border-box; }
  html, body { width: 1200px; height: 960px; overflow: hidden; }
  body { background: var(--stage); position: relative; font-family: "Open Sans", Arial, sans-serif; }

  .card {
    position: absolute;
    width: 600px;
    height: 343px;
    box-shadow: 0 2px 6px rgba(0,0,0,0.45);
  }
  .card--front { left: 314px; top: 113px; background: var(--card-white); }
  .card--back {
    left: 311px; top: 472px;
    background: radial-gradient(ellipse 62% 68% at 50% 48%, #2aa3dc 0%, #1b7fc0 45%, var(--deep) 100%);
  }

  .brand {
    position: absolute;
    left: 0; right: 0;
    display: flex;
    align-items: center;
    justify-content: center;
    gap: 12px;
  }
  .card--front .brand { top: 78px; }
  .card--back .brand { top: 128px; }
  .brand__dot { width: 34px; height: 34px; border-radius: 50%; }
  .brand__name { font-size: 40px; font-weight: 600; letter-spacing: -0.5px; line-height: 1; }
  .card--front .brand__dot { background: var(--bright); }
  .card--front .brand__name { color: var(--brand-blue); }
  .card--back .brand__dot { background: #ffffff; }
  .card--back .brand__name { color: #ffffff; }

  .person {
    position: absolute;
    top: 189px; left: 0; right: 0;
    text-align: center;
  }
  .person__name {
    font-family: "Roboto Condensed", "Arial Narrow", sans-serif;
    font-weight: 700; font-size: 21px; color: var(--navy); letter-spacing: 0.3px;
  }
  .person__title {
    font-family: "Roboto Condensed", "Arial Narrow", sans-serif;
    font-weight: 700; font-size: 16px; color: var(--sky); margin-top: 0;
  }

  .contact {
    position: absolute;
    top: 246px; left: 50%;
    transform: translateX(-50%);
    width: 360px;
    border-top: 1px solid var(--rule);
    border-bottom: 1px solid var(--rule);
    padding: 4px 0 5px;
    text-align: center;
    font-size: 14px;
    color: var(--text-grey);
    white-space: nowrap;
  }
  .contact__label { font-weight: 700; color: var(--navy); }

  .website {
    position: absolute;
    top: 287px; left: 0; right: 0;
    text-align: center;
    font-weight: 700; font-size: 14px;
    color: var(--sky);
    letter-spacing: 0.3px;
  }
</style>
</head>
<body>
  <section class="card card--front">
    <div class="brand">
      <span class="brand__dot"></span>
      <span class="brand__name">Brightvale Global</span>
    </div>
    <div class="person">
      <div class="person__name">MARLA OSTROV</div>
      <div class="person__title">CEO</div>
    </div>
    <div class="contact">
      <span class="contact__label">P.</span> 310-447-2093
      <span class="contact__label">E.</span>bvgcorp7@mailnest.example
    </div>
    <div class="website">WWW.BRIGHTVALE.EXAMPLE</div>
  </section>

  <section class="card card--back">
    <div class="brand">
      <span class="brand__dot"></span>
      <span class="brand__name">Brightvale Global</span>
    </div>
  </section>
</body>
</html>
```